Stationery design for a Saas platform at PR industry

Hello, Corvanta is a media database and press release distribution platform targeting Public Relations agencies and corporates. We started at Turkey and moved our HQ to San Francisco, US. We changed our website and need a new stationary design with compatible of the hew website. Our website address is http://www.corvanta-example.com/en
Updates
Reason: The number of the designers are not enough for us. Looking for some other good designs.
Industry/Entity Type
Industry
Requirements
Must have
- Statinery covers business card design, letterhead, envalope, file and invoice design.

```html
<!DOCTYPE html>
<html lang="en">
<head>
<meta charset="utf-8">
<title>Corvanta Business Cards</title>
<link href="https://fonts.googleapis.com/css2?family=Open+Sans:wght@400;600&display=swap" rel="stylesheet">
<style>
  :root {
    --backdrop: #5a4c44;
    --card: #141414;
    --card-edge: #0a0a0a;
    --ink-light: #d9d9d9;
    --ink-soft: #bdbdbd;
    --emboss: #3a3a3a;
    --foil: #a9a9a9;
    --rule: #8a8a8a;
  }
  * { margin: 0; padding: 0; box-sizing: border-box; }
  html, body {
    width: 1200px; height: 1200px; overflow: hidden;
    background: var(--backdrop);
    font-family: "Open Sans", sans-serif;
  }
  .stage { position: relative; width: 1200px; height: 1200px; }

  .card {
    position: absolute;
    width: 520px; height: 300px;
    background: var(--card);
    border-radius: 4px;
    box-shadow: 0 6px 0 var(--card-edge), 0 14px 30px rgba(0,0,0,0.45);
  }
  .card--front { left: 70px; top: 330px; }
  .card--back  { left: 610px; top: 570px; }

  .brand {
    display: flex; align-items: center; gap: 12px;
    font-weight: 600; letter-spacing: 0.5px;
  }
  .brand__dot { border-radius: 50%; flex: none; }

  .card--front .brand {
    position: absolute; left: 50%; top: 50%;
    transform: translate(-50%, -50%);
    font-size: 50px; color: var(--emboss);
  }
  .card--front .brand__dot { width: 46px; height: 46px; background: var(--foil); }

  .card--back .brand {
    position: absolute; left: 34px; top: 118px;
    font-size: 38px; color: var(--ink-light);
  }
  .card--back .brand__dot { width: 36px; height: 36px; background: var(--ink-light); }

  .divider {
    position: absolute; left: 292px; top: 74px;
    width: 1px; height: 150px; background: var(--rule);
  }

  .contact {
    position: absolute; left: 308px; top: 78px;
    color: var(--ink-soft); font-size: 12.5px; line-height: 1.45;
  }
  .contact__name {
    color: var(--ink-light); font-weight: 600; font-size: 15px;
    text-transform: uppercase; letter-spacing: 0.6px;
  }
  .contact__title { margin-bottom: 10px; }
  .contact__address { margin-bottom: 10px; }
  .contact__row { display: flex; align-items: center; gap: 7px; }
  .contact__row svg { width: 11px; height: 11px; flex: none; fill: none; stroke: var(--ink-soft); stroke-width: 1.4; }
</style>
</head>
<body>
<div class="stage">

  <section class="card card--front">
    <div class="brand"><span class="brand__dot"></span><span class="brand__name">Corvanta</span></div>
  </section>

  <section class="card card--back">
    <div class="brand"><span class="brand__dot"></span><span class="brand__name">Corvanta</span></div>
    <div class="divider"></div>
    <div class="contact">
      <p class="contact__name">Daniel Reyes</p>
      <p class="contact__title">Founder/CEO</p>
      <p class="contact__address">210 Harbor Lane, Bayview<br>P.O. Box 412, Market Avenue</p>
      <p class="contact__row">
        <svg viewBox="0 0 12 12"><path d="M3 1.5 L4.8 4 L3.8 5.2 Q5 7.4 6.8 8.2 L8 7.2 L10.5 9 L9.5 10.5 Q4.5 10 1.5 3 Z"/></svg>
        415-555-0134
      </p>
      <p class="contact__row">
        <svg viewBox="0 0 12 12"><rect x="1" y="2.5" width="10" height="7"/><path d="M1 2.5 L6 6.5 L11 2.5"/></svg>
        hello@corvanta-example.com
      </p>
      <p class="contact__row">
        <svg viewBox="0 0 12 12"><circle cx="6" cy="6" r="4.7"/><ellipse cx="6" cy="6" rx="2" ry="4.7"/><path d="M1.3 6 H10.7"/></svg>
        www.corvanta-example.com
      </p>
    </div>
  </section>

</div>
</body>
</html>
```